VENTURE CAPITAL GROUP BUSINESS CARD DESIGN

Venture Capital Group based in SF looking for a bold business card design. No trendy colour explosion, 3D effects etc. Just "simple" optical effects. Works on your brain, keeps your eye focused and sticks to your mind.
Target Market(s)
Technology startups
Industry/Entity Type
Venture Capital
Contact Information for Business Card
BARNABY WHITLOCK
MANAGING PARTNER
817 FERN ST SAN FRANCISCO, CA 94111
415.555.0143 O
415.555.0167 F
415.555.0192 C
barn@halcyonridgefund.example

```html
<!DOCTYPE html>
<html lang="en">
<head>
<meta charset="utf-8">
<title>Halcyon Ridge Fund – Business Card</title>
<link rel="stylesheet" href="https://fonts.googleapis.com/css2?family=Open+Sans:ital,wght@0,400;0,600;0,700;1,300;1,400;1,600;1,700&family=Roboto+Condensed:wght@700&display=swap">
<style>
  :root {
    --band-green: #077a30;
    --brand-green: #14923a;
    --rule-navy: #1f1f8f;
    --ink: #111111;
    --ink-soft: #333333;
    --label-grey: #8a8a8a;
    --paper: #ffffff;
    --disc-light: #ffffff;
    --disc-dark: #dcdcdc;
  }
  html, body {
    margin: 0;
    padding: 0;
    width: 1200px;
    height: 686px;
    overflow: hidden;
    background: var(--paper);
  }
  .card {
    position: relative;
    width: 1200px;
    height: 686px;
    background: var(--paper);
    overflow: hidden;
    font-family: "Open Sans", Arial, sans-serif;
  }
  .side-band {
    position: absolute;
    left: 0; top: 0;
    width: 142px; height: 686px;
    background: var(--band-green);
  }
  .firm-title {
    position: absolute;
    left: 175px; width: 987px;
    top: 56px;
    margin: 0;
    text-align: center;
    font-weight: 700;
    font-size: 37px;
    letter-spacing: 0.5px;
    color: var(--brand-green);
  }
  .rule {
    position: absolute;
    left: 175px; width: 987px;
    height: 1px;
    background: var(--rule-navy);
  }
  .rule-top { top: 114px; }
  .rule-bottom { top: 604px; }
  .brand-mark {
    position: absolute;
    left: 185px; top: 150px;
    width: 340px; height: 270px;
  }
  .brand-mark svg { position: absolute; left: 90px; top: 0; }
  .brand-name {
    position: absolute;
    left: 0; width: 340px;
    top: 208px;
    margin: 0;
    text-align: center;
    font-weight: 600;
    font-size: 30px;
    letter-spacing: 1px;
    color: var(--brand-green);
  }
  .person {
    position: absolute;
    left: 155px; top: 476px;
  }
  .person-name {
    margin: 0;
    font-family: "Roboto Condensed", "Arial Narrow", sans-serif;
    font-weight: 700;
    font-size: 36px;
    line-height: 44px;
    color: var(--ink);
  }
  .person-role {
    margin: 6px 0 0;
    font-style: italic;
    font-weight: 400;
    font-size: 29px;
    line-height: 40px;
    color: var(--brand-green);
    letter-spacing: 0.5px;
  }
  .contact {
    position: absolute;
    right: 23px; top: 374px;
    margin: 0; padding: 0;
    list-style: none;
    text-align: right;
    font-style: italic;
    font-size: 25px;
    line-height: 44px;
  }
  .contact-label { color: var(--label-grey); font-weight: 400; }
  .contact-value { color: var(--ink-soft); font-weight: 700; }
</style>
</head>
<body>
<div class="card">
  <div class="side-band"></div>

  <h1 class="firm-title">HALCYON RIDGE FUND</h1>
  <div class="rule rule-top"></div>

  <div class="brand-mark">
    <svg width="160" height="160" viewBox="0 0 160 160" aria-hidden="true">
      <defs>
        <radialGradient id="disc-shade" cx="40%" cy="40%" r="65%">
          <stop offset="0" stop-color="var(--disc-light)"/>
          <stop offset="1" stop-color="var(--disc-dark)"/>
        </radialGradient>
      </defs>
      <circle cx="80" cy="80" r="78" fill="url(#disc-shade)"/>
    </svg>
    <p class="brand-name">HALCYON RIDGE</p>
  </div>

  <div class="person">
    <p class="person-name">BARNABY WHITLOCK</p>
    <p class="person-role">MANAGING PARTNER</p>
  </div>

  <ul class="contact">
    <li><span class="contact-value">817 Fern St San Francisco, CA 94111</span></li>
    <li><span class="contact-label">Office: </span><span class="contact-value">415.555.0143</span></li>
    <li><span class="contact-label">Fax: </span><span class="contact-value">415.555.0167</span></li>
    <li><span class="contact-label">Contact: </span><span class="contact-value">415.555.0192</span></li>
    <li><span class="contact-label">E-mail: </span><span class="contact-value">barn@halcyonridgefund.example</span></li>
  </ul>

  <div class="rule rule-bottom"></div>
</div>
</body>
</html>
```